E-Commerce Website Update for Bamboo Poles Company

Existing website at:

http://www.reedcraftstudio.example/
http://www.reedcraftstudio.example/pages/product-and-price-list

Two pages to design: home page and "price list" page.

Info for home page as follows:

HOME PAGE:

Header:
Company Name: reedcraft studio
Telephone: 1 888 412 5093

Across the top:
Home | Price List | Blog | FAQ | About | Contact

Down the side:
About Bamboo
Wedding Arbors
Bamboo For Flutes
Black Bamboo
Spotted Bamboo
Bamboo Carpentry
Photo Gallery
All Products & Prices
Blog
FAQ
About
Contact

Should have shopping cart and search buttons on top.
Please see ai file, attached for logo (leaf) and font
In addition the homepage should have one or two sections for promotions

Chosen design will be asked to help deign a PRODUCT AND PRICE LIST page similar to the one we have now, but with "LEARN MORE" and "ORDER NOW" buttons for each item.
Updates

Reason: Thanks  for all the designs so far; giving an extra week for extra consideration.

Target Market(s)

Consumers, wedding planners.

Industry/Entity Type

Shopping

Requirements
Must have
• Clean, easy to read design.
Should not have
• No flash animation.

```html
<!DOCTYPE html>
<html lang="en">
<head>
<meta charset="utf-8">
<title>reedcraft studio – Price List</title>
<link rel="stylesheet" href="https://fonts.googleapis.com/css2?family=Ubuntu:wght@400;500;700&family=Open+Sans:wght@400;600&family=Arimo:wght@400;700&display=swap">
<style>
:root{
  --green:#6fbf2f;
  --green-dark:#4e9a1c;
  --ink:#222;
  --text:#555;
  --muted:#888;
  --line:#d4d4d4;
  --row:#ececec;
  --nav-top:#3a3a3a;
  --nav-bottom:#0d0d0d;
  --white:#fff;
}
*{box-sizing:border-box;margin:0;padding:0}
html,body{width:1200px;height:1200px;overflow:hidden;background:var(--white)}
body{font-family:"Ubuntu",sans-serif;color:var(--text)}
.page{position:relative;width:1024px;height:1024px;transform:scale(1.171875);transform-origin:0 0}
.abs{position:absolute}

/* header */
.brand{left:53px;top:16px;font-family:"Open Sans",sans-serif;font-weight:400;font-size:36px;line-height:33px;color:var(--ink);letter-spacing:-0.5px}
.phone-label{left:470px;top:21px;width:124px;text-align:center;font-family:"Arimo",sans-serif;font-weight:700;font-size:17px;color:#8a8a8a;white-space:nowrap}
.phone-row{left:358px;top:44px;display:flex;align-items:center;gap:12px;white-space:nowrap}
.phone-icon{flex:none;width:37px;height:37px;border-radius:6px;background:linear-gradient(#7fcf45,#4ea21f);display:flex;align-items:center;justify-content:center}
.phone-number{font-family:"Arimo",sans-serif;font-weight:700;font-size:36px;line-height:40px;color:var(--green);white-space:nowrap}
.cart{left:812px;top:41px;display:flex;gap:8px;white-space:nowrap}
.cart-icon{width:28px;height:29px;border:1px solid #ddd;border-radius:4px;background:linear-gradient(#fff,#eee);display:flex;align-items:center;justify-content:center}
.cart-title{font-size:11.5px;font-weight:700;color:#333}
.cart-info{font-size:11.5px;color:#555;margin-top:3px;letter-spacing:0.3px}
.cart-info a{color:var(--green);margin-left:14px}

/* nav */
.nav{left:52px;top:105px;width:920px;height:45px;border-radius:7px;background:linear-gradient(var(--nav-top),var(--nav-bottom) 60%);display:flex;align-items:center}
.nav ul{list-style:none;display:flex;padding-left:19px}
.nav li{font-size:12.5px;color:var(--white);padding:0 17px 0 0;margin-right:18px;border-right:1px solid #555;line-height:14px;white-space:nowrap}
.nav li:last-child{border:none}
.search{position:absolute;left:621px;top:8px;width:229px;height:29px;border-radius:7px;background:var(--white);font-size:12px;color:#555;padding:8px 10px;white-space:nowrap}
.search-go{position:absolute;left:860px;top:8px;width:49px;height:29px;border-radius:6px;background:linear-gradient(#7fd040,#3f8f14);color:var(--white);font-weight:700;font-size:13px;display:flex;align-items:center;justify-content:center}

/* sidebar */
.categories{left:52px;top:160px;width:250px;height:321px;border:1px solid var(--line);border-radius:3px}
.box-title{display:flex;align-items:center;gap:9px;padding-left:15px;height:32px;font-size:12px;font-weight:700;color:#333;white-space:nowrap}
.bullet{width:9px;height:9px;border-radius:2px;background:var(--green);position:relative}
.bullet::after{content:"";position:absolute;left:3px;top:2px;border-left:4px solid var(--white);border-top:2.5px solid transparent;border-bottom:2.5px solid transparent}
.categories .box-title{border-bottom:1px solid var(--line)}
.cat-list{list-style:none;padding:8px 0 0 20px}
.cat-list li{font-size:12px;color:#555;height:22px;line-height:14px;display:flex;gap:5px;letter-spacing:0.3px;white-space:nowrap}
.cat-list li::before{content:"";margin-top:3px;border-left:4px solid var(--green);border-top:3.5px solid transparent;border-bottom:3.5px solid transparent;height:0}

.promo{left:52px;top:490px;width:250px;height:182px;border:2px solid #ddd;border-radius:7px;background:#f1f1f1;overflow:hidden}
.promo-photo{position:absolute;left:4px;top:4px;width:238px;height:143px;border-radius:5px;background:linear-gradient(160deg,#e9ebe6 0%,#cfc59a 45%,#b89a4e 70%,#e4e4e2 100%)}
.promo-badge{position:absolute;left:138px;top:2px;width:104px;height:96px;border-radius:50%;background:radial-gradient(#6fbf2f,#3f8d15);color:var(--white);text-align:center;font-family:"Arimo",sans-serif;font-weight:700;line-height:1}
.promo-badge .pct{display:block;font-size:34px;margin-top:14px}
.promo-badge .off{display:block;font-size:24px;margin-top:2px}
.promo-caption{position:absolute;left:0;right:0;top:152px;text-align:center;font-family:"Arimo",sans-serif;font-weight:700;font-size:17px;color:#7cc447;white-space:nowrap}

/* product tables */
.section-title{left:312px;width:660px;height:35px;border:1px solid var(--line);border-radius:3px}
.section-title .box-title{height:33px}
.table-head{left:422px;width:550px;height:25px;border:1px solid var(--line);border-radius:3px;display:flex;align-items:center;font-size:11.5px;font-weight:700;color:#333;letter-spacing:0.3px;white-space:nowrap}
.col-item{width:60px;padding-left:8px}
.col-desc{width:100px}
.col-dim{width:110px}
.col-price{width:90px}
.table-head .col-item{width:69px}
.product{left:312px;width:660px;height:100px;display:flex;gap:10px}
.product-photo{width:100px;height:100px;border:1px solid #ddd}
.product-row{flex:1;background:var(--row);display:flex;align-items:center;font-size:11.5px;color:#555;letter-spacing:0.4px;white-space:nowrap}
.product-row .col-item{width:69px}

/* footer */
.footer-line{left:52px;top:991px;width:920px;height:2px;background:var(--green)}
.copyright{right:52px;top:1001px;font-family:"Open Sans",sans-serif;font-size:10.5px;color:#777;white-space:nowrap}
</style>
</head>
<body>
<div class="page">

  <header>
    <div class="abs brand">reedcraft<br>studio</div>

    <div class="abs phone-label">Toll Free</div>
    <div class="abs phone-row">
      <div class="phone-icon">
        <svg width="22" height="22" viewBox="0 0 24 24"><path fill="#fff" d="M6.6 10.8c1.4 2.8 3.8 5.1 6.6 6.6l2.2-2.2c.3-.3.7-.4 1-.2 1.1.4 2.3.6 3.6.6.6 0 1 .4 1 1V20c0 .6-.4 1-1 1C10.6 21 3 13.4 3 4c0-.6.4-1 1-1h3.5c.6 0 1 .4 1 1 0 1.3.2 2.5.6 3.6.1.3 0 .7-.2 1z"/></svg>
      </div>
      <div class="phone-number">1 888 412 5093</div>
    </div>

    <div class="abs cart">
      <div class="cart-icon">
        <svg width="16" height="14" viewBox="0 0 16 14"><path d="M1 1h2.5l2 8h7.5l1.5-6H4.3" fill="none" stroke="#999" stroke-width="1.3"/><circle cx="6.5" cy="12" r="1.2" fill="#999"/><circle cx="12" cy="12" r="1.2" fill="#999"/></svg>
      </div>
      <div>
        <div class="cart-title">Shopping Cart:</div>
        <div class="cart-info">0 products <a href="#">view cart</a></div>
      </div>
    </div>
  </header>

  <nav class="abs nav">
    <ul>
      <li>Home</li><li>Price List</li><li>Blog</li><li>FAQ</li><li>About</li><li>Contact</li>
    </ul>
    <div class="search">Search keyword here</div>
    <div class="search-go">GO!</div>
  </nav>

  <aside>
    <div class="abs categories">
      <div class="box-title"><span class="bullet"></span>Categories</div>
      <ul class="cat-list">
        <li>About Bamboo</li><li>Wedding Arbors</li><li>Bamboo For Flutes</li><li>Black Bamboo</li>
        <li>Spotted Bamboo</li><li>Bamboo Carpentry</li><li>Photo Gallery</li><li>All Products &amp; Prices</li>
        <li>Blog</li><li>FAQ</li><li>About</li><li>Contact</li>
      </ul>
    </div>

    <div class="abs promo">
      <div class="promo-photo" role="img" aria-label="Photo of cut large bamboo pole sections with green leaves"></div>
      <div class="promo-badge"><span class="pct">20%</span><span class="off">OFF</span></div>
      <div class="promo-caption">4” x 8’ $14.00/pole</div>
    </div>
  </aside>

  <main>
    <div class="abs section-title" style="top:160px"><div class="box-title"><span class="bullet"></span>Bamboo Poles</div></div>
    <div class="abs table-head" style="top:205px"><span class="col-item">Item#</span><span class="col-desc">Description</span><span class="col-dim">Dimensions</span><span class="col-price">Pole Price</span><span>Packing/Carton Price</span></div>

    <div class="abs product" style="top:240px">
      <div class="product-photo" role="img" aria-label="Thin reed bamboo poles" style="background:linear-gradient(90deg,#dfe6d2,#b9b86a,#e1e6d6,#a9a95a,#dde4d0)"></div>
      <div class="product-row"><span class="col-item">C1</span><span class="col-desc">Reed Bamboo</span><span class="col-dim">3/8"dia. × 60"</span><span class="col-price">$0.53</span><span>15 poles, $8.00/cartonPrice</span></div>
    </div>
    <div class="abs product" style="top:350px">
      <div class="product-photo" role="img" aria-label="Natural bamboo poles" style="background:linear-gradient(90deg,#b4a847,#d9ce80,#a99c3a,#d6cb7a,#b0a444)"></div>
      <div class="product-row"><span class="col-item">C3</span><span class="col-desc">Reed Bamboo</span><span class="col-dim">3/8"dia. × 60"</span><span class="col-price">$0.53</span><span>15 poles, $8.00/cartonPrice</span></div>
    </div>
    <div class="abs product" style="top:460px">
      <div class="product-photo" role="img" aria-label="Pale bamboo poles" style="background:linear-gradient(90deg,#c9c487,#e4e0b0,#bdb774,#e1dca8,#c6c080)"></div>
      <div class="product-row"><span class="col-item">C4</span><span class="col-desc">Reed Bamboo</span><span class="col-dim">3/8"dia. × 60"</span><span class="col-price">$0.53</span><span>15 poles, $8.00/cartonPrice</span></div>
    </div>

    <div class="abs section-title" style="top:580px"><div class="box-title"><span class="bullet"></span>Black Poles</div></div>
    <div class="abs table-head" style="top:625px"><span class="col-item">Item#</span><span class="col-desc">Description</span><span class="col-dim">Dimensions</span><span class="col-price">Pole Price</span><span>Packing/Carton Price</span></div>

    <div class="abs product" style="top:660px">
      <div class="product-photo" role="img" aria-label="Bamboo poles with nodes" style="background:linear-gradient(90deg,#d4cd8c,#b7ac55,#dcd596,#b3a852,#d6cf8e)"></div>
      <div class="product-row"><span class="col-item">T2</span><span class="col-desc">Reed Bamboo</span><span class="col-dim">3/8"dia. × 60"</span><span class="col-price">$0.53</span><span>15 poles, $8.00/cartonPrice</span></div>
    </div>
    <div class="abs product" style="top:770px">
      <div class="product-photo" role="img" aria-label="Bamboo poles with nodes" style="background:linear-gradient(90deg,#d2cb88,#b9ae58,#dad394,#b5aa54,#d4cd8b)"></div>
      <div class="product-row"><span class="col-item">T4</span><span class="col-desc">Reed Bamboo</span><span class="col-dim">3/8"dia. × 60"</span><span class="col-price">$0.53</span><span>15 poles, $8.00/cartonPrice</span></div>
    </div>
    <div class="abs product" style="top:880px">
      <div class="product-photo" role="img" aria-label="Light tan bamboo poles" style="background:linear-gradient(90deg,#e6dcc2,#cdbb93,#e8dfc6,#cbb88e,#e4d9bd)"></div>
      <div class="product-row"><span class="col-item">M1</span><span class="col-desc">Reed Bamboo</span><span class="col-dim">3/8"dia. × 60"</span><span class="col-price">$0.53</span><span>15 poles, $8.00/cartonPrice</span></div>
    </div>
  </main>

  <footer>
    <div class="abs footer-line"></div>
    <div class="abs copyright">© 2011 Reedcraft Studio</div>
  </footer>

</div>
</body>
</html>
```